Website for Sports and Exercise Medicine Doctor with active research in stem cells therapies.

I am a sports and exercise medicine doctor with research interests in the cutting edge areas of biological therapies, most notable stem cells. None of my patients are dying of anything, and most of them come to see me to decrease their pain, so they can get back to what they want to do.

The approach i then take is to decrease their pain and support them to achieve the things they wish to achieve. Most people start at "Just make it stop hurting doc" , but I try to move them towards something more important over time.

I would like the website to be very different to other "Doctor or medical websites" in its look. No pictures of doctors in white coats and no pictures of fit old people smiling. I would potentially like the fist thing seen to be a quote:

"Less pain. Everybody wants it, but what are you going to do, once you've got it?"

(But this is only an idea, I am open to anything)

The website will need a couple of things

1. "Locations" I work
2. "Research" I am involved in
3. "Sort Me out" - Clinical information for people to access
4. "Social" - imbedded chirpline and friendgrid
5. "Blog" - imbedded postmill blog
6. "Bio" - the usual bio-stuff

The "Sort Me out" - pages I would like to have the functionality as seen in this site http://www.vandrolix.com.au/platelet/. I intend to put disease topics into these pages (eg Achilles tehdinopathy, osteoarthritis etc etc etc). Once again I am not wedded to this but something along these lines would be good.

To give you an idea these are some sites I like
http://www.harborlantern.com/
http://quimbet.com/
http://orvanstudio.com.sg/
http://milbonhonestkettle.com/
http://www.tessmonthly.com/
http://gravwick.com/#offering
http://pelicanworks.tv/
http://tidalnova.com/
http://foxledger.co.uk/#about

Target Market(s)

20-80 year old.
People with tendon injuries
People with osteoarthritis
People interested in stem cells
I will build the site over time to contain information on multiple sporting injuries and musculoskeletal disorders. It will also become a site for the latest on stem cell research particularly in the area of osteoarthritis.

Industry/Entity Type

Medical

Font styles to use
Sans Serif

Colors
ffffff

Requirements
Nice to have
• To give you an idea these are some sites I like
http://quimbet.com/
http://pelicanworks.tv/
http://tidalnova.com/
Should not have
• Pictures of doctors in white coats or old fit people smiling

```html
<!DOCTYPE html>
<html lang="en">
<head>
<meta charset="utf-8">
<title>Corvane — Sports &amp; Exercise Medicine</title>
<link rel="stylesheet" href="https://fonts.googleapis.com/css2?family=Montserrat:wght@400;600&family=PT+Sans+Narrow:wght@400;700&family=Raleway:wght@300;400;500&display=swap">
<style>
:root{
  --teal:#3e7a8c;
  --teal-dark:#2f6577;
  --teal-text:#2d6f86;
  --ink:#2b2b2b;
  --body:#555;
  --paper:#ffffff;
  --mist:#f3f5f6;
  --blog-bg:#3b3b3b;
  --footer:#262626;
  --nav-active:#2d8bb0;
}
*{margin:0;padding:0;box-sizing:border-box}
html,body{width:1200px;height:4114px;overflow:hidden;background:var(--paper)}
body{font-family:"Montserrat",sans-serif;color:var(--body);position:relative}
.block{position:absolute;left:0;width:1200px}

/* header */
.site-header{top:0;height:120px;background:var(--paper);border-bottom:1px solid #e4e8ea}
.brand{position:absolute;left:150px;top:30px;display:flex;align-items:center;gap:14px}
.brand-dot{width:44px;height:44px;border-radius:50%;border:3px solid var(--teal-text)}
.brand-name{font-family:"Raleway",sans-serif;font-weight:400;font-size:34px;color:var(--teal-text)}
.main-nav{position:absolute;left:395px;top:40px;display:flex;gap:0}
.main-nav a{font-size:17px;letter-spacing:.5px;color:var(--teal-text);text-decoration:none;padding:10px 18px;font-weight:400}
.main-nav a.active{color:var(--nav-active);background:#eef3f5}

/* hero */
.hero{top:120px;height:675px;background:linear-gradient(90deg,#fafbfb 0%,#f1f4f5 40%,#e6ebee 100%)}
.hero-photo{position:absolute;left:420px;top:0;width:720px;height:675px;background:radial-gradient(ellipse at 50% 45%,#c9b7a8 0%,#d8dde0 45%,#eef1f2 75%,rgba(241,244,245,0) 100%)}
.hero-quote{position:absolute;left:145px;top:48px;width:500px}
.hero-quote .lead{font-family:"Raleway",sans-serif;font-weight:300;font-size:34px;color:#444}
.hero-quote .q{font-family:"Raleway",sans-serif;font-weight:500;font-size:33px;line-height:1.3;color:#333;margin-top:14px}
.hero-quote p{font-size:14px;line-height:1.6;color:#666;margin-top:22px;width:420px}
.hero-arrow{position:absolute;top:280px}
.hero-arrow.prev{left:22px}.hero-arrow.next{right:22px}

/* social bands */
.band{background:linear-gradient(180deg,var(--teal) 0%,var(--teal-dark) 100%);color:#fff;text-align:center}
.band-mark{margin:70px auto 0;width:130px;height:130px;border-radius:50%;border:3px solid rgba(255,255,255,.85)}
.band-name{font-size:18px;font-weight:600;letter-spacing:1px;margin-top:18px}
.band p{font-size:14px;line-height:1.55;width:870px;margin:22px auto 0;color:#e8f1f4}
.band-friendgrid{top:795px;height:371px}
.band-chirpline{top:1715px;height:377px}
.band-bio{top:2640px;height:378px}

/* feature rows */
.feature{background:linear-gradient(180deg,#fff 0%,#f4f6f7 100%)}
.feature-media{position:absolute;top:0;height:100%}
.feature-copy{position:absolute;top:70px;width:520px}
.eyebrow{font-size:16px;font-weight:600;letter-spacing:1px;color:var(--teal-text)}
.feature h3{font-family:"PT Sans Narrow",sans-serif;font-weight:400;font-size:38px;color:var(--teal-text);line-height:1.1;margin-top:6px}
.feature h2{font-family:"PT Sans Narrow",sans-serif;font-weight:700;font-size:48px;color:var(--ink);line-height:1.05}
.feature p{font-size:14px;line-height:1.65;margin-top:22px;color:#666}
.feature-sort{top:1166px;height:549px}
.feature-sort .feature-media{left:0;width:560px;background:linear-gradient(90deg,#d9c9b7 0%,#e6ddd2 55%,rgba(244,246,247,0) 100%)}
.feature-sort .feature-copy{left:548px}
.feature-research{top:2092px;height:548px}
.feature-research .feature-media{right:0;width:600px;background:linear-gradient(270deg,#6f8f5a 0%,#a86a5c 35%,#d6d9db 70%,rgba(244,246,247,0) 100%)}
.feature-research .feature-copy{left:148px;top:85px}
.feature-locations{top:3018px;height:548px}
.feature-locations .feature-media{left:0;width:560px;background:linear-gradient(90deg,#e7e9e6 0%,#eef0ec 60%,rgba(244,246,247,0) 100%)}
.feature-locations .feature-copy{left:548px}

/* blog */
.blog{top:3566px;height:479px;background:var(--blog-bg)}
.blog-tab{position:absolute;left:490px;top:0;width:220px;height:50px;background:#e9e9e9;color:#333;font-size:20px;font-weight:600;text-align:center;line-height:50px;border-radius:0 0 4px 4px}
.blog-band{position:absolute;top:0;left:0;width:1200px;height:60px;background:linear-gradient(180deg,#8a8a8a,#5a5a5a)}
.blog-cards{position:absolute;top:90px;left:148px;display:flex;gap:45px}
.blog-card{width:280px}
.blog-card .thumb{height:192px;border:6px solid #fff;background:linear-gradient(135deg,#e1d3c3,#c9a48a 60%,#b48570)}
.blog-card time{display:block;color:#eee;font-size:15px;margin-top:14px}
.blog-card p{color:#bbb;font-size:13px;line-height:1.5;margin-top:6px}
.share{display:flex;gap:8px;margin-top:12px}
.share span{font-size:11px;color:#444;background:#e8e8e8;padding:3px 10px;border-radius:2px}

/* footer */
.site-footer{top:4045px;height:69px;background:var(--footer)}
.site-footer small{position:absolute;left:148px;top:26px;color:#aaa;font-size:13px}
.footer-social{position:absolute;right:150px;top:17px;display:flex;gap:10px}
.footer-social span{width:36px;height:36px;border-radius:50%;background:var(--teal)}
</style>
</head>
<body>

<header class="block site-header">
  <div class="brand"><span class="brand-dot"></span><span class="brand-name">Corvane</span></div>
  <nav class="main-nav">
    <a class="active" href="#">HOME</a><a href="#">ABOUT US</a><a href="#">SERVICES</a><a href="#">SORT ME OUT</a><a href="#">BLOG</a><a href="#">LOCATIONS</a>
  </nav>
</header>

<section class="block hero">
  <div class="hero-photo" role="img" aria-label="Photo of a therapist helping a woman stretch her leg in a clinic"></div>
  <div class="hero-quote">
    <div class="lead">Less pain. Everybody wants it.</div>
    <div class="q">But what are you going to do, once you've got it?"</div>
    <p>Fusce ullamcorper dapibus semper. Nullam vestibulum eleifend tellus, vel ullamcorper leo. Donec blandit vel felis at volutpat. Nunc porta justo eget urna tempor, id placerat nisi.</p>
  </div>
  <svg class="hero-arrow prev" width="20" height="40" viewBox="0 0 20 40"><path d="M16 4 4 20l12 16" fill="none" stroke="#2d6f86" stroke-width="3"/></svg>
  <svg class="hero-arrow next" width="20" height="40" viewBox="0 0 20 40"><path d="M4 4l12 16L4 36" fill="none" stroke="#2d6f86" stroke-width="3"/></svg>
</section>

<section class="block band band-friendgrid">
  <div class="band-mark"></div>
  <div class="band-name">friendgrid</div>
  <p>ornare sed ipsum. Vivamus vel cursus massa, vel varius eros. Quisque ante mi, lacinia ut viverra et, vehicula in nunc. Class aptent taciti sociosqu ad litora torquent per conubia nostra, per inceptos himenaeos. Maecenas id gravida dolor</p>
</section>

<section class="block feature feature-sort">
  <div class="feature-media" role="img" aria-label="Photo of a clinician treating a patient's knee in a bright treatment room"></div>
  <div class="feature-copy">
    <div class="eyebrow">SORT ME OUT</div>
    <h3>Consectetur adipiscing elit</h3>
    <h2>luctus justo libero bibendum,</h2>
    <p>Nulla adipiscing turpis purus, vel malesuada ligula consequat in. Nulla volutpat ante eget hendrerit fringilla. Ut tortor ligula, vestibulum sit amet vulputate eget, accumsan sit amet ligula. Etiam in tortor suscipit, luctus leo ac, interdum odio. Quisque aliquam ultrices facilisis. Nam velit metus, ultricies non dignissim ut, consectetur vitae dui. Integer placerat urna nibh, eu ultricies ante congue at.</p>
  </div>
</section>

<section class="block band band-chirpline">
  <div class="band-mark"></div>
  <div class="band-name">chirpline</div>
  <p>ornare sed ipsum. Vivamus vel cursus massa, vel varius eros. Quisque ante mi, lacinia ut viverra et, vehicula in nunc. Class aptent taciti sociosqu ad litora torquent per conubia nostra, per inceptos himenaeos. Maecenas id gravida dolor</p>
</section>

<section class="block feature feature-research">
  <div class="feature-media" role="img" aria-label="Photo of an injured football player lying on the grass being attended to"></div>
  <div class="feature-copy">
    <div class="eyebrow">RESEARCH</div>
    <h3>Ornare sed ipsum Vivamus</h3>
    <h2>Vel varius er Quisque ante mi,</h2>
    <p>Nulla adipiscing turpis purus, vel malesuada ligula consequat in. Nulla volutpat ante eget hendrerit fringilla. Ut tortor ligula, vestibulum sit amet vulputate eget, accumsan sit amet ligula. Etiam in tortor suscipit, luctus leo ac, interdum odio. Quisque aliquam ultrices facilisis. Nam velit metus, ultricies non dignissim ut, consectetur vitae dui. Integer placerat urna nibh, eu ultricies ante congue at.</p>
  </div>
</section>

<section class="block band band-bio">
  <div class="band-mark"></div>
  <div class="band-name">BIO-STUFF</div>
  <p>ornare sed ipsum. Vivamus vel cursus massa, vel varius eros. Quisque ante mi, lacinia ut viverra et, vehicula in nunc. Class aptent taciti sociosqu ad litora torquent per conubia nostra, per inceptos himenaeos. Maecenas id gravida dolor</p>
</section>

<section class="block feature feature-locations">
  <div class="feature-media" role="img" aria-label="Street map showing the clinic locations"></div>
  <div class="feature-copy">
    <div class="eyebrow">LOCATIONS</div>
    <h3>Consectetur adipiscing elit</h3>
    <h2>luctus justo libero bibendum,</h2>
    <p>Nulla adipiscing turpis purus, vel malesuada ligula consequat in. Nulla volutpat ante eget hendrerit fringilla. Ut tortor ligula, vestibulum sit amet vulputate eget, accumsan sit amet ligula. Etiam in tortor suscipit, luctus leo ac, interdum odio. Quisque aliquam ultrices facilisis. Nam velit metus, ultricies non dignissim ut, consectetur vitae dui. Integer placerat urna nibh, eu ultricies ante congue at.</p>
  </div>
</section>

<section class="block blog">
  <div class="blog-band" role="img" aria-label="Faded photo strip of a treatment session"></div>
  <div class="blog-tab">Featured Blog</div>
  <div class="blog-cards">
    <article class="blog-card">
      <div class="thumb" role="img" aria-label="Photo of a clinician treating a patient's knee"></div>
      <time>January 2, 2013</time>
      <p>Ornare sed ipsum cursus massa vehicula in nunc. Class aptent.</p>
      <div class="share"><span>Share</span><span>Post</span></div>
    </article>
    <article class="blog-card">
      <div class="thumb" role="img" aria-label="Photo of a clinician treating a patient's knee"></div>
      <time>January 2, 2013</time>
      <p>Ornare sed ipsum cursus massa vehicula in nunc. Class aptent.</p>
      <div class="share"><span>Share</span><span>Post</span></div>
    </article>
    <article class="blog-card">
      <div class="thumb" role="img" aria-label="Photo of a clinician treating a patient's knee"></div>
      <time>January 2, 2013</time>
      <p>Ornare sed ipsum cursus massa vehicula in nunc. Class aptent.</p>
      <div class="share"><span>Share</span><span>Post</span></div>
    </article>
  </div>
</section>

<footer class="block site-footer">
  <small>Copyright ©2013 Corvane.com All rights reserved.</small>
  <div class="footer-social"><span aria-label="friendgrid"></span><span aria-label="chirpline"></span><span aria-label="video channel"></span></div>
</footer>

</body>
</html>
```